Kestowell Chardonnay Wine Label 2024

We need a wine label design for a small, family-owned vineyard in Broke, Hunter Valley of NSW (Australia). The vineyard is called Kestowell and we have an existing logo and 'brand book' for the vineyard home that is rented out for short stay bookings. This is attached and includes font style, colour palette and our Kestowell logo for the accommodation (we're not wedded to this but also probably not after a completely different rethink either as we want the accommodation and the wine to feel part of the same thing.

Project:
The initial label requirement (front and back) is for the Kestowell 2024 Chardonnay, which is called 'Marigold'. The label would need to be able to extend to other varietals (eg Verdehlo and Sparkling) in 2025. Attached is draft copy for front and back for the 2024 Chardonnay as a guide.

STYLE: We like a relatively simple, classic design and have played with both a dark (navy) and a light background (white/cream). Based on the final label design we will order a Tarquo colour to pick up on the label theme.

The Chardonnay bottle dimensions are attached, as is our logo file (if that helps)

Target Market(s)

online 25-50 yearold

Industry/Entity Type

Wine

Requirements
Must have
• front and back label design Kestowell logo and name

```html
<!DOCTYPE html>
<html lang="en">
<head>
<meta charset="utf-8">
<title>Kestowell Marigold 2024 Chardonnay – Labels</title>
<link rel="stylesheet" href="https://fonts.googleapis.com/css2?family=Cinzel:wght@400;500&family=Crimson+Text:wght@400&display=swap">
<style>
  :root {
    --backdrop: #cdcbcc;
    --navy: #3b4558;
    --gold: #968a78;
    --ivory: #f1eee8;
    --faint: rgba(255,255,255,0.07);
  }
  * { margin: 0; padding: 0; box-sizing: border-box; }
  html, body { width: 783px; height: 1200px; overflow: hidden; }
  body { background: var(--backdrop); position: relative; font-family: "Crimson Text", serif; color: var(--ivory); }

  .label {
    position: absolute;
    left: 199px;
    width: 385px;
    background: var(--navy);
    overflow: hidden;
    box-shadow: 0 1px 3px rgba(0,0,0,0.18);
  }
  .label--front { top: 41px; height: 549px; }
  .label--back  { top: 614px; height: 548px; }

  .label__decor { position: absolute; inset: 0; width: 100%; height: 100%; }

  .brand-mark {
    position: absolute;
    display: flex;
    align-items: center;
    gap: 7px;
    font-family: "Crimson Text", serif;
    color: var(--ivory);
    line-height: 1;
  }
  .brand-mark__dot { width: 8px; height: 8px; border-radius: 50%; background: var(--ivory); }

  .front__brand { left: 0; right: 0; top: 84px; justify-content: center; font-size: 31px; }

  .wine-name {
    position: absolute;
    font-family: "Cinzel", serif;
    font-weight: 500;
    color: var(--gold);
    line-height: 1;
    letter-spacing: 0.01em;
  }
  .front__name { left: 0; right: 0; top: 164px; text-align: center; font-size: 40px; line-height: 45px; }

  .front__variety {
    position: absolute; left: 0; right: 0; top: 337px;
    text-align: center;
    font-family: "Cinzel", serif;
    font-size: 18px; line-height: 22px;
    color: var(--ivory);
  }
  .front__volume {
    position: absolute; left: 0; right: 0; top: 496px;
    text-align: center;
    font-family: "Cinzel", serif;
    font-size: 17px;
    color: var(--ivory);
  }

  .back__name { left: 28px; top: 57px; font-size: 29px; line-height: 33px; }
  .back__brand { right: 30px; top: 83px; font-size: 24px; }

  .back__copy {
    position: absolute; left: 20px; right: 20px; top: 170px;
    text-align: center;
    font-size: 12px; line-height: 14.7px;
  }
  .back__vintage { margin-bottom: 14.7px; }
  .back__contact { margin-top: 14.7px; }

  .back__mandatory {
    position: absolute; left: 26px; top: 389px;
    font-size: 12px; line-height: 14.7px;
    list-style: none;
  }
  .back__mandatory li::before { content: "• "; }
</style>
</head>
<body>

<section class="label label--front" aria-label="Front label">
  <svg class="label__decor" viewBox="0 0 385 549" aria-hidden="true">
    <circle cx="150" cy="560" r="170" fill="var(--gold)"/>
  </svg>
  <div class="brand-mark front__brand"><span>Kestowell</span><span class="brand-mark__dot"></span></div>
  <h1 class="wine-name front__name">Kestowell<br>Marigold</h1>
  <p class="front__variety">2024 Chardonnay<br>Hunter Valley</p>
  <p class="front__volume">750ml</p>
</section>

<section class="label label--back" aria-label="Back label">
  <svg class="label__decor" viewBox="0 0 385 548" aria-hidden="true">
    <circle cx="150" cy="560" r="170" fill="var(--faint)"/>
  </svg>
  <h2 class="wine-name back__name">Kestowell<br>Marigold</h2>
  <div class="brand-mark back__brand"><span>Kestowell</span><span class="brand-mark__dot"></span></div>

  <div class="back__copy">
    <p class="back__vintage">2024 Chardonnay</p>
    <p>New ownership in 2019 marked the regeneration of the<br>
    35-year-old vineyard and the launch of Kestowell Wines.<br>
    Capturing the spirit of the Marigold, this ‘old dame’ block at<br>
    the heart of the vineyard has emerged with new life and<br>
    vigour after years of dry to create a notable wine, celebrating<br>
    the power of renewal and the gift of time.<br>
    The 2024 Marigold is an elegantly oaked, estate-grown<br>
    Chardonnay displaying flavours of white peach, cinnamon<br>
    and cashews, with a smooth texture and lengthy citrus finish.</p>
    <p class="back__contact">12 Tallow Lane, Broke, NSW<br>www.kestowell-wines.com</p>
  </div>

  <ul class="back__mandatory">
    <li style="list-style:none" class="back__mandatory-title"></li>
  </ul>
  <div class="back__mandatory">
    <p>Mandatory requirements:</p>
    <ul style="list-style:none">
      <li>Pregnancy warning</li>
      <li>Standard drinks – 8.3</li>
      <li>Alcohol 13.55 Vol. 750ml</li>
      <li>Preservatives: Sulfites (220)</li>
      <li>No allergens added.</li>
      <li>This wine is vegan friendly.</li>
    </ul>
  </div>
</section>

</body>
</html>
```